I need a label with logo to go on jars of honey.
Label size 70mm x 70mm
The front label should say :
The Tall Fern Honey Co. (logo)
Tarepo Honey
400g
The back label:
Would have nutritional information
And our address
You can see from the uploaded files the styles I prefer, I have uploaded a photo of the honey product too. The background of the logo doesn't have to be white. I would like to develop a color scheme that would look nice against the color of the honey.
Logo Text
The Tall Fern Honey Co. / The Tall Fern Honey Company

```html
<!DOCTYPE html>
<html lang="en">
<head>
<meta charset="utf-8">
<title>Tarepo Honey – Jar Labels</title>
<link href="https://fonts.googleapis.com/css2?family=Archivo:wght@500;700;900&family=Barlow+Condensed:wght@500;600&family=Bebas+Neue&display=swap" rel="stylesheet">
<style>
  :root {
    --stage: #222224;
    --label-bg: #ffffff;
    --band-orange: #f9ab28;
    --band-orange-deep: #f59a1e;
    --comb-orange: #f7a12e;
    --comb-peach: #fbe1c2;
    --ink: #111111;
    --ink-soft: #3b3b3d;
    --title-grey-top: #8f9095;
    --title-grey-bottom: #2c2c2e;
    --honey-yellow: #f9c80e;
    --honey-orange: #f39530;
    --honey-red: #ee5a3a;
    --amber-light: #f3a53c;
    --amber-dark: #c0621e;
  }
  * { box-sizing: border-box; margin: 0; padding: 0; }
  html, body { width: 1200px; height: 719px; overflow: hidden; }
  body { background: var(--stage); position: relative; font-family: "Archivo", Arial, sans-serif; }

  .label {
    position: absolute; top: 125px; width: 469px; height: 469px;
    background: var(--label-bg); overflow: hidden;
    box-shadow: 6px 10px 18px rgba(0,0,0,.55);
  }
  .label--front { left: 140px; }
  .label--back { left: 622px; }

  .top-band {
    position: absolute; left: 0; top: 0; width: 100%; height: 71px;
    background: linear-gradient(180deg, var(--band-orange), var(--band-orange-deep));
  }
  .comb-top {
    position: absolute; left: 0; top: 71px; width: 100%; height: 70px;
    background: linear-gradient(180deg, rgba(247,161,46,.75), rgba(247,161,46,0));
  }
  .label--back .comb-top {
    background: linear-gradient(90deg, rgba(247,161,46,.7) 0 10%, transparent 12% 88%, rgba(247,161,46,.7) 90%);
  }
  .comb-bottom {
    position: absolute; left: 0; bottom: 0; width: 100%; height: 130px;
    background: linear-gradient(180deg, rgba(251,225,194,0), var(--comb-peach) 45%);
  }

  .brand {
    position: absolute; left: 0; width: 100%; top: 12px; text-align: center;
    font-family: "Barlow Condensed", sans-serif; font-weight: 600;
    font-size: 22px; line-height: 22px; color: var(--ink);
  }

  .product-name {
    position: absolute; left: 60px; top: 140px; width: 300px;
    font-family: "Bebas Neue", sans-serif; text-align: center;
    line-height: 0.95;
  }
  .product-name span { display: block; -webkit-background-clip: text; background-clip: text; color: transparent; }
  .product-name__place {
    font-size: 106px;
    background-image: linear-gradient(180deg, var(--title-grey-top), var(--title-grey-bottom));
  }
  .product-name__kind {
    font-size: 110px;
    background-image: linear-gradient(180deg, var(--honey-yellow), var(--honey-orange) 65%, var(--honey-red));
  }

  .honey-dipper-art {
    position: absolute; left: 362px; top: 204px; width: 107px; height: 257px;
    background: linear-gradient(160deg, var(--amber-light), var(--amber-dark));
    opacity: .9;
  }

  .net-weight {
    position: absolute; left: 0; width: 100%; top: 408px; text-align: center;
    font-family: "Barlow Condensed", sans-serif; font-weight: 600;
    font-size: 46px; letter-spacing: 1px; color: var(--ink);
  }

  .nutrition {
    position: absolute; left: 32px; top: 39px; width: 404px; height: 228px;
    background: #fff; border: 7px solid var(--ink); padding: 4px 13px 0 13px;
    color: var(--ink);
  }
  .nutrition__title { font-weight: 900; font-size: 37px; line-height: 36px; padding-left: 3px; letter-spacing: .3px; }
  .nutrition__serving { font-weight: 700; font-size: 13.5px; padding-left: 3px; line-height: 16px; }
  .nutrition__row {
    display: flex; justify-content: space-between; align-items: center;
    font-weight: 700; font-size: 13.5px; padding: 0 6px 0 3px;
    border-top: 1.2px solid var(--ink); height: 25px;
  }
  .nutrition__row--thick { border-top-width: 3px; }
  .nutrition__row--first { margin-top: 6px; }
  .nutrition__dv { justify-content: flex-end; height: 27px; font-weight: 500; }
  .nutrition__row b { font-weight: 700; }

  .blurb {
    position: absolute; left: 40px; width: 389px; top: 280px; text-align: center;
    font-family: Arial, "Archivo", sans-serif; font-size: 13.6px; line-height: 19.5px; color: var(--ink);
  }
  .contact {
    position: absolute; left: 0; width: 100%; top: 402px; text-align: center;
    font-family: "Barlow Condensed", sans-serif; font-weight: 500;
    font-size: 22px; line-height: 23px; color: var(--ink-soft);
  }
</style>
</head>
<body>

<section class="label label--front">
  <div class="top-band"></div>
  <div class="comb-top" role="img" aria-label="orange honeycomb cells hanging from the top band"></div>
  <div class="comb-bottom" role="img" aria-label="pale peach honeycomb pattern along the bottom"></div>
  <p class="brand">The Tall Fern<br>Honey Co.</p>
  <h1 class="product-name">
    <span class="product-name__place">Tarepo</span>
    <span class="product-name__kind">Honey</span>
  </h1>
  <div class="honey-dipper-art" role="img" aria-label="illustration area: honey dipper with dripping honey and a bee"></div>
  <p class="net-weight">400G</p>
</section>

<section class="label label--back">
  <div class="top-band"></div>
  <div class="comb-top" role="img" aria-label="orange honeycomb cells at both sides"></div>
  <div class="comb-bottom" role="img" aria-label="pale peach honeycomb pattern along the bottom"></div>

  <div class="nutrition">
    <h2 class="nutrition__title">Nutrition Facts</h2>
    <p class="nutrition__serving">Serving Size 1tbsp (21g)</p>
    <div class="nutrition__row nutrition__row--thick nutrition__row--first">Amount Per Srving</div>
    <div class="nutrition__row">Calories 64</div>
    <div class="nutrition__row nutrition__row--thick nutrition__dv">%Daily Value*</div>
    <div class="nutrition__row"><span>Total Fat 0g</span><b>0%</b></div>
    <div class="nutrition__row"><span>Sodium 0mg</span><b>0%</b></div>
    <div class="nutrition__row"><span>Protein 0g</span><b>0%</b></div>
  </div>

  <p class="blurb">Lorem ipsum dolor sit amet, consectetuer adipiscing elit, sed diam nonummy nibh euismod tincidunt ut laoreet dolore magna aliquam erat volutpat. Ut wisi enim ad minim veniam,</p>

  <p class="contact">Address: your addres here please, address.<br>Ph: 01234567890 | web:thetallfernhoneyco.</p>
</section>

</body>
</html>
```